Brisk Mend's Blow Their Mind Website

We own a group of cell phone and tablet repair shops in the bay area that is emerging into the mobile device insurance industry and want to develop a site that is clean, organized, and efficient at communicating who we are, the services we provide and the positive feedback we have been getting from our clients. As we enter into this new field of business, Our goal is to attract larger corporate accounts.

We want our home screen to have a big focus on the protection plan for the devices right away much like the home screen from these links:

http://www.gadgetvault.com/

and also - https://us.keepitsnug.com/smartphone-protection.html

We also need to make our repair services clear, here is a website of a company that does repair and we want to highlight both ends of the business.

ww.fixnovo.com

So the home screen will include the tab categories at the top of the screen
home/ protection /repair /about /contact

The first portion will be protection and as you scroll down there will be the next section about repair and following that will be information about the company.

Target Market(s)

Individuals that would be looking for pricing, clients that come to our store, but ultimately the heavy hitters we would want to attract would be larger corporate accounts so the message we want to communicate is professional, organized and credible in the services we provide.

Industry/Entity Type

Cell Phone

Number of Pages Required

5+ page

Font styles to use
Serif

Colors
34a6d7

Requirements
Must have
• Eye catching, organized, with the wow factor that a business will look at our site and will be able to tell that we know what looks good and what grabs peoples attention. A large emphasis on the protection plan section like the links we provided and an organized home screen with the sections highlighted in the project description
• Tabs with links to different sections of the business such as protection that will go into detail about our protections plans and why our plan is best
• repair with a menu of the different prices we provide for different devices and services for that device
• an about us tab
• a contact us tab
Nice to have
• Artistic flow on the homescreen that the different sections flow together without looking too cookie cutter
• Wow factor
Should not have
• Clutter, confusion, disorganization, cheesy cookie cutter

```html
<!DOCTYPE html>
<html lang="en">
<head>
<meta charset="utf-8">
<title>Brisk Mend – Smartphone Protection &amp; Repair</title>
<link href="https://fonts.googleapis.com/css2?family=Raleway:wght@300;400;600;700;800&family=Open+Sans:wght@400;600;700&display=swap" rel="stylesheet">
<style>
:root{
  --blue:#34a6d7;
  --blue-bright:#1fb0ec;
  --dark:#2b2e33;
  --darker:#1f2226;
  --ink:#333a40;
  --muted:#8a9096;
  --line:#e1e4e7;
  --panel:#f3f4f6;
  --grey-head:#5d6166;
  --white:#ffffff;
}
*{box-sizing:border-box;margin:0;padding:0}
html,body{width:1200px;height:4164px;overflow:hidden}
body{font-family:"Open Sans",Arial,sans-serif;color:var(--ink);background:var(--white);font-size:14px;line-height:1.6}
h1,h2,h3,h4{font-family:"Raleway",Arial,sans-serif}
.wrap{width:1000px;margin:0 auto;position:relative}

/* top bar + header */
.topbar{height:22px;background:#f5f6f7;border-bottom:1px solid var(--line);font-size:11px;color:var(--muted)}
.topbar .wrap{display:flex;gap:22px;align-items:center;height:22px}
.header{height:58px;background:var(--white);border-bottom:1px solid var(--line)}
.header .wrap{display:flex;align-items:center;justify-content:space-between;height:58px}
.brand{display:flex;align-items:center;gap:10px;font-family:"Raleway",sans-serif;font-weight:700;font-size:22px;color:var(--blue)}
.brand .dot{width:22px;height:22px;border-radius:50%;background:var(--blue)}
.nav{display:flex;gap:34px;font-family:"Raleway",sans-serif;font-size:11px;font-weight:700;letter-spacing:1px;color:#555}
.nav a{color:inherit;text-decoration:none;display:flex;flex-direction:column;align-items:center;gap:4px}
.nav a::before{content:"";width:14px;height:10px;border:2px solid #aab0b5;border-radius:2px}
.nav a.active{color:var(--blue)}
.nav a.active::before{border-color:var(--blue)}

/* hero */
.hero{height:540px;background:linear-gradient(100deg,#eef3f7 0%,#dfe8ef 45%,#b9cad8 100%);position:relative;overflow:hidden}
.hero .wrap{height:540px}
.hero-text{position:absolute;left:0;top:42px;width:430px}
.hero-text h1{font-size:40px;font-weight:600;color:var(--ink);line-height:1.15;margin-bottom:14px}
.hero-text p{font-size:14px;color:#555;margin-bottom:16px}
.hero-list{list-style:none;margin-bottom:40px}
.hero-list li{display:flex;align-items:center;gap:10px;font-size:14px;margin-bottom:4px}
.hero-list li::before{content:"✓";width:16px;height:16px;border-radius:50%;background:var(--dark);color:#fff;font-size:10px;display:flex;align-items:center;justify-content:center}
.btn{display:inline-block;padding:10px 22px;font-size:12px;font-weight:600;color:#fff;text-decoration:none;border-radius:2px}
.btn-dark{background:var(--dark)}
.btn-blue{background:var(--blue-bright)}
.hero-buttons{display:flex;gap:30px}
.hero-photo{position:absolute;left:430px;top:20px;width:560px;height:500px;border-radius:10px;background:linear-gradient(160deg,#f8fafc 0%,#d5e3ee 55%,#a8c3d8 100%)}
.price-badge{position:absolute;left:790px;top:160px;width:150px;height:150px;border-radius:50%;background:var(--blue-bright);color:#fff;text-align:center;display:flex;flex-direction:column;justify-content:center;box-shadow:0 0 0 8px rgba(255,255,255,.4)}
.price-badge small{font-size:14px}
.price-badge strong{font-family:"Raleway",sans-serif;font-size:38px;line-height:1}
.deduct-badge{position:absolute;left:660px;top:330px;width:100px;height:100px;border-radius:50%;background:var(--dark);color:#fff;text-align:center;display:flex;flex-direction:column;justify-content:center;font-size:11px;line-height:1.2}
.deduct-badge strong{font-size:22px;font-family:"Raleway",sans-serif}
.arrow{position:absolute;top:240px;width:24px;height:40px}
.arrow.left{left:24px}.arrow.right{right:24px}
.dots{position:absolute;left:50%;bottom:14px;transform:translateX(-50%);display:flex;gap:8px}
.dots span{width:9px;height:9px;border-radius:50%;background:rgba(255,255,255,.7)}
.dots span.on{background:var(--dark)}

/* section heads */
.sec-title{text-align:center;font-size:32px;font-weight:400;letter-spacing:1px;color:var(--ink)}
.sec-title b{font-weight:800}
.sec-lead{text-align:center;width:620px;margin:10px auto 0;font-size:13px;color:var(--muted);line-height:1.5}

/* features */
.features{height:580px;padding-top:74px;background:var(--white)}
.feature-grid{width:640px;margin:50px auto 0;display:grid;grid-template-columns:1fr 1fr;row-gap:40px;column-gap:40px}
.feature{display:flex;align-items:center;gap:20px;height:80px}
.feature.left{justify-content:flex-end;text-align:right}
.feature .ico{width:80px;height:80px;border-radius:50%;background:var(--blue-bright);flex:none;display:flex;align-items:center;justify-content:center}
.feature span{font-weight:600;font-size:14px;width:130px}

/* compare */
.compare{height:760px;background:var(--panel);padding-top:70px}
.compare-table{width:840px;margin:40px auto 0;border-collapse:collapse;background:#fff;font-size:11px}
.compare-table th{height:110px;color:#fff;font-weight:400;font-size:14px;vertical-align:middle;text-align:center;font-family:"Raleway",sans-serif}
.compare-table th strong{display:block;font-size:32px;font-weight:700;line-height:1.1}
.compare-table th small{font-size:11px}
.compare-table th.blank{background:transparent}
.compare-table th.rival{background:var(--grey-head);border:1px solid #4d5156}
.compare-table th.ours{background:var(--blue-bright);position:relative}
.compare-table td{height:30px;border:1px solid var(--line);padding:0 10px;color:#666}
.compare-table td.c{text-align:center}
.compare-table td.ours{color:var(--blue);background:#f4fbfe}
.compare-table tr.tall td{height:70px}
.tick{color:var(--blue);font-weight:700}

/* cta band */
.band{height:100px;background:var(--blue-bright);margin-top:120px}
.band .wrap{display:flex;justify-content:space-between;align-items:center;height:100px}
.band h3{font-size:26px;font-weight:400;color:#fff}
.band .btn{background:#fff;color:var(--ink)}

/* repair */
.repair{height:660px;padding-top:60px}
.repair-body{position:relative;width:1000px;margin:40px auto 0;height:420px}
.repair-list{position:absolute;left:-20px;top:0;width:460px;list-style:none}
.repair-list li{display:flex;gap:18px;height:100px;margin-bottom:8px}
.repair-list .ico{width:80px;height:100px;background:#6f747a;flex:none;display:flex;align-items:center;justify-content:center}
.repair-list li:first-child .ico{background:var(--blue-bright)}
.repair-list h4{font-size:13px;font-weight:700;margin-top:8px;letter-spacing:.5px}
.repair-list p{font-size:12px;color:var(--muted);line-height:1.4;width:180px}
.repair-photo{position:absolute;left:440px;top:0;width:520px;height:430px;background:linear-gradient(180deg,#dfe3e6,#8a9299);border-radius:4px}

/* models band */
.models{height:280px;background:linear-gradient(100deg,#cfd3d6 0%,#8c9197 50%,#5c6167 100%);color:#fff;text-align:center;position:relative}
.models .models-photo{position:absolute;left:100px;top:20px;width:360px;height:240px;border-radius:6px;background:linear-gradient(180deg,#a7b0b8,#6a7178)}
.models .txt{position:absolute;left:560px;top:90px;width:480px}
.models .txt p{font-size:18px;font-weight:300}
.models .txt h3{font-size:26px;font-weight:800;letter-spacing:1px;margin-bottom:20px}

/* testimonials */
.people{height:600px;padding-top:90px}
.quotes{width:980px;margin:50px auto 0;display:grid;grid-template-columns:repeat(3,1fr);gap:30px}
.quote .box{border:1px solid var(--line);padding:22px;font-size:13px;color:#666;height:170px;position:relative}
.quote.mid .box{border-color:var(--blue)}
.quote .box::after{content:"";position:absolute;left:40px;bottom:-9px;width:16px;height:16px;background:#fff;border-right:1px solid var(--line);border-bottom:1px solid var(--line);transform:rotate(45deg)}
.quote.mid .box::after{border-color:var(--blue)}
.who{display:flex;align-items:center;gap:14px;margin-top:22px;padding-left:10px}
.avatar{width:60px;height:60px;border-radius:50%;background:linear-gradient(160deg,#d9c9b8,#9d8e80)}
.who strong{display:block;color:var(--blue);font-size:14px}
.who small{color:var(--muted);font-size:11px}

/* footer */
.footer{height:444px;background:var(--darker);color:#9aa0a6;font-size:12px}
.foot-top{height:110px;border-bottom:1px solid #34383d}
.foot-top .wrap{display:flex;align-items:center;height:110px;gap:20px}
.foot-ico{width:40px;height:40px;border:2px solid #777;border-radius:4px;flex:none}
.foot-top h4{color:#fff;font-size:13px;font-weight:600;width:80px;line-height:1.3}
.foot-top p{width:300px;font-size:11px;line-height:1.4}
.subscribe{display:flex}
.subscribe span{width:170px;height:30px;background:#fff}
.subscribe b{background:var(--blue-bright);color:#fff;height:30px;padding:0 16px;display:flex;align-items:center;font-weight:600}
.foot-cols{display:grid;grid-template-columns:1.1fr 1fr 1fr 1fr;gap:30px;padding-top:40px;height:260px}
.foot-cols h5{color:#fff;font-family:"Raleway",sans-serif;font-size:14px;font-weight:600;margin-bottom:14px}
.foot-cols ul{list-style:none}
.foot-cols li{margin-bottom:6px}
.foot-cols .brand{font-size:17px;margin-bottom:14px}
.foot-cols .brand .dot{width:16px;height:16px}
.photo-grid{display:grid;grid-template-columns:repeat(3,60px);gap:6px}
.photo-grid span{height:50px;background:#3a3f45}
.foot-bottom{border-top:1px solid #34383d;height:74px}
.foot-bottom .wrap{display:flex;justify-content:space-between;align-items:center;height:74px;font-size:11px}
.social{display:flex;gap:10px}
.social span{width:14px;height:14px;border-radius:50%;background:#5a5f65}
</style>
</head>
<body>

<div class="topbar"><div class="wrap"><span>⊙ Login</span><span>⊙ Register</span></div></div>

<header class="header">
  <div class="wrap">
    <div class="brand"><span class="dot"></span>Brisk Mend</div>
    <nav class="nav">
      <a class="active" href="#">HOME</a>
      <a href="#">PROTECTION</a>
      <a href="#">REPAIR</a>
      <a href="#">ABOUT</a>
      <a href="#">CONTACT</a>
    </nav>
  </div>
</header>

<section class="hero">
  <svg class="arrow left" viewBox="0 0 24 40"><path d="M18 4 4 20l14 16" fill="none" stroke="#fff" stroke-width="3"/></svg>
  <svg class="arrow right" viewBox="0 0 24 40"><path d="M6 4l14 16L6 36" fill="none" stroke="#fff" stroke-width="3"/></svg>
  <div class="wrap">
    <div class="hero-text">
      <h1>Smartphone<br>Protection Plan</h1>
      <p>We don't care where you bought your phone, which carrier you have or if it's more than 30 days old. With us, you're covered.</p>
      <ul class="hero-list">
        <li>Covers phones up to 2 years old</li>
        <li>Next-day claims resolution</li>
        <li>Unlimited claims</li>
        <li>Low $75 deductible on all models</li>
      </ul>
      <div class="hero-buttons"><a class="btn btn-dark" href="#">Read More Info</a><a class="btn btn-blue" href="#">Get a Quote</a></div>
    </div>
    <div class="hero-photo" role="img" aria-label="Smartphone with a cracked screen resting on a light surface"></div>
    <div class="deduct-badge">Only<strong>$75</strong>deductible</div>
    <div class="price-badge"><small>Starting at</small><strong>$5.99</strong><small>/mo</small></div>
  </div>
  <div class="dots"><span class="on"></span><span></span><span></span><span></span><span></span></div>
</section>

<section class="features">
  <h2 class="sec-title">KEY FEATURES ABOUT <b>PROTECTION</b></h2>
  <p class="sec-lead">One simple plan for every phone you own. Fast claims, fair prices and real people ready to help you whenever your device needs it most.</p>
  <div class="feature-grid">
    <div class="feature left"><span>One focus</span><div class="ico"><svg width="36" height="24" viewBox="0 0 36 24"><path d="M2 12C8 2 28 2 34 12 28 22 8 22 2 12z" fill="none" stroke="#fff" stroke-width="2.5"/><circle cx="18" cy="12" r="5" fill="#fff"/></svg></div></div>
    <div class="feature"><div class="ico"><svg width="34" height="30" viewBox="0 0 34 30"><path d="M17 2 32 28H2z" fill="#fff"/><path d="M17 11v8" stroke="#1fb0ec" stroke-width="3"/><circle cx="17" cy="23" r="1.8" fill="#1fb0ec"/></svg></div><span>Cracked screens &amp; accidental damage</span></div>
    <div class="feature left"><span>Next-day claims resolution</span><div class="ico"><svg width="34" height="34" viewBox="0 0 34 34"><circle cx="17" cy="17" r="14" fill="none" stroke="#fff" stroke-width="3"/><path d="M17 9v9l6 4" fill="none" stroke="#fff" stroke-width="3"/></svg></div></div>
    <div class="feature"><div class="ico"><svg width="34" height="34" viewBox="0 0 34 34"><circle cx="13" cy="13" r="8" fill="none" stroke="#fff" stroke-width="4" stroke-dasharray="4 3"/><circle cx="24" cy="24" r="6" fill="none" stroke="#fff" stroke-width="3" stroke-dasharray="3 2"/></svg></div><span>Mechanical breakdowns</span></div>
    <div class="feature left"><span>Liquid &amp; water damage</span><div class="ico"><svg width="24" height="32" viewBox="0 0 24 32"><path d="M12 2C6 12 3 17 3 21a9 9 0 0 0 18 0c0-4-3-9-9-19z" fill="#fff"/></svg></div></div>
    <div class="feature"><div class="ico"><svg width="32" height="32" viewBox="0 0 32 32"><rect x="3" y="6" width="26" height="23" rx="2" fill="none" stroke="#fff" stroke-width="3"/><path d="M3 13h26M10 2v8M22 2v8" stroke="#fff" stroke-width="3"/></svg></div><span>Flexible protection</span></div>
  </div>
</section>

<section class="compare">
  <h2 class="sec-title">COMPARE US – <b>PROTECTING</b> AN NOVA 6</h2>
  <p class="sec-lead">See how our plan measures up against other providers. Lower monthly cost, faster claims and coverage that really fits your phone.</p>
  <table class="compare-table">
    <tr>
      <th class="blank" style="width:240px"></th>
      <th class="rival">CareGuard<strong>$8.25</strong><small>/month</small></th>
      <th class="rival">TradeShield<strong>$8</strong><small>/month</small></th>
      <th class="ours">Brisk Mend<strong>$5.99</strong><small>/month</small></th>
    </tr>
    <tr><td>Accidental damage</td><td class="c tick">✓</td><td class="c tick">✓</td><td class="c ours tick">✓</td></tr>
    <tr><td>Mechanical breakdown</td><td class="c tick">✓</td><td class="c tick">✓</td><td class="c ours tick">✓</td></tr>
    <tr><td>Liquid damage</td><td class="c tick">✓</td><td class="c tick">✓</td><td class="c ours tick">✓</td></tr>
    <tr><td>Coverage term</td><td class="c">24 months</td><td class="c">24 months</td><td class="c ours">Unlimited</td></tr>
    <tr><td>Deductible</td><td class="c">$79</td><td class="c">$99</td><td class="c ours">$75</td></tr>
    <tr><td>Claims limit</td><td class="c">2 claims</td><td class="c">Unlimited</td><td class="c ours">Unlimited</td></tr>
    <tr><td>Claims time</td><td class="c">3–5 days</td><td class="c">2–3 days</td><td class="c ours">Next day</td></tr>
    <tr class="tall"><td>Cancellation</td><td class="c">Pay upfront, refund only within first 30 days</td><td class="c">Refund of the unused part minus a fee</td><td class="c ours">Cancel any time, no questions asked</td></tr>
    <tr class="tall"><td>Cancellation fees</td><td class="c">—</td><td class="c">$25 admin fee</td><td class="c ours">None</td></tr>
  </table>
</section>

<section class="band" style="margin-top:0">
  <div class="wrap"><h3>Get Excellent Services for your Phone</h3><a class="btn" href="#">Get a Quote Now</a></div>
</section>

<section class="repair">
  <h2 class="sec-title">WELL-ROUNDED <b>REPAIR</b></h2>
  <p class="sec-lead">From cracked glass to dead batteries, our certified technicians repair most phones and tablets the same day, with parts you can trust.</p>
  <div class="repair-body">
    <ul class="repair-list">
      <li><div class="ico"><svg width="24" height="38" viewBox="0 0 24 38"><rect x="2" y="2" width="20" height="34" rx="3" fill="none" stroke="#fff" stroke-width="3"/><circle cx="12" cy="30" r="2" fill="#fff"/></svg></div><div><h4>SCREEN REPLACEMENT</h4><p>Cracked screen? We replace it fast with quality parts.</p></div></li>
      <li><div class="ico"><svg width="40" height="22" viewBox="0 0 40 22"><rect x="2" y="2" width="32" height="18" rx="2" fill="none" stroke="#fff" stroke-width="3"/><rect x="34" y="7" width="4" height="8" fill="#fff"/><rect x="6" y="6" width="14" height="10" fill="#fff"/></svg></div><div><h4>BATTERY REPLACEMENT</h4><p>Phone not holding a charge like it used to?</p></div></li>
      <li><div class="ico"><svg width="24" height="32" viewBox="0 0 24 32"><path d="M12 2C6 12 3 17 3 21a9 9 0 0 0 18 0c0-4-3-9-9-19z" fill="#fff"/></svg></div><div><h4>WATER DAMAGE</h4><p>If your phone fell in the water, get it to us now.</p></div></li>
      <li><div class="ico"><svg width="22" height="36" viewBox="0 0 22 36"><path d="M14 2 3 20h8l-3 14 11-19h-8z" fill="#fff"/></svg></div><div><h4>POWER BUTTON</h4><p>Stuck power button repair is one of our specialties.</p></div></li>
    </ul>
    <div class="repair-photo" role="img" aria-label="A phone with a shattered screen beside the same phone fully repaired, joined by a blue arrow"></div>
  </div>
</section>

<section class="models">
  <div class="models-photo" role="img" aria-label="Smartphone splashing into water"></div>
  <div class="txt">
    <p>Tab Repair, Droid-type, &amp; Nova phone Repairs</p>
    <h3>MOST PHONE MODELS REPAIRED</h3>
    <a class="btn btn-dark" href="#">Get Started Now</a>
  </div>
</section>

<section class="people">
  <h2 class="sec-title">PEOPLE <b>SAYS</b></h2>
  <div class="quotes">
    <div class="quote"><div class="box">My screen shattered on a Monday and the team had it fixed by lunch. Friendly staff, fair price and the phone works like new. I signed our whole office up for the protection plan right after.</div><div class="who"><div class="avatar" role="img" aria-label="Customer portrait"></div><div><strong>Liam Porter</strong><small>New York, United States</small></div></div></div>
    <div class="quote mid"><div class="box">Filing a claim took five minutes and I had a working phone the very next day. No hidden fees, no long calls. This is exactly the kind of service a busy business needs from a partner.</div><div class="who"><div class="avatar" role="img" aria-label="Customer portrait"></div><div><strong>Nora Blake</strong><small>Melbourne, Australia</small></div></div></div>
    <div class="quote"><div class="box">Dropped my phone in the sink and thought it was gone for good. They brought it back to life and saved all my photos. Honest advice and quick work, I would recommend them to anyone.</div><div class="who"><div class="avatar" role="img" aria-label="Customer portrait"></div><div><strong>Owen Mercer</strong><small>Glasgow, Scotland</small></div></div></div>
  </div>
</section>

<footer class="footer">
  <div class="foot-top"><div class="wrap">
    <span class="foot-ico"></span><h4>Latest Posts</h4>
    <p>Five simple habits that keep your phone safe, plus our new plan for business fleets is now live.</p>
    <span class="foot-ico" style="margin-left:40px"></span><h4>Sign up Newsletter</h4>
    <div class="subscribe"><span></span><b>Subscribe</b></div>
  </div></div>
  <div class="wrap foot-cols">
    <div>
      <div class="brand"><span class="dot"></span>Brisk Mend</div>
      <ul><li>210 Harbor Lane, Suite 4</li><li>Bayview, CA 94000</li><li>(555) 014-2290</li><li>hello@briskmend.example</li></ul>
    </div>
    <div><h5>Useful Links</h5><ul><li>› Protection Plans</li><li>› Repair Prices</li><li>› Business Accounts</li><li>› File a Claim</li><li>› Contact Us</li></ul></div>
    <div><h5>About Us</h5><p>We run a group of phone and tablet repair shops across the bay area and now protect devices for people and companies of every size.</p><p style="margin-top:10px">Read more ›</p></div>
    <div><h5>Photo Stream</h5><div class="photo-grid" role="img" aria-label="Grid of recent shop photos"><span></span><span></span><span></span><span></span><span></span><span></span></div></div>
  </div>
  <div class="foot-bottom"><div class="wrap">
    <span>Copyright © 2015 briskmend.example. All rights reserved. Terms of Use | Privacy Policy</span>
    <div class="social"><span></span><span></span><span></span><span></span><span></span><span></span></div>
  </div></div>
</footer>

</body>
</html>
```